Brightacre - online store for farm produce

Online store selling fresh produce (vegetables, fruits, dairy products, meat, ...) from various farmers. Every farm has its own shopping window - order page - just like a really simple web store.

Please check the attached design brief and mock-ups for further details.

Target Market(s)

People looking for fresh vegetables, fruit, meat, ... delivered from farms

Industry/Entity Type

Farming

Coding

Coded - Design and coding required

Number of Pages Required

5+ page

Font styles to use
Sans Serif

Requirements
Must have
• Custom design. Good UX/UI design, very functional.
Responsive using bootstrap 12 point grid system

```html
<!DOCTYPE html>
<html lang="en">
<head>
<meta charset="utf-8">
<title>Brightacre – Fresh Farm Produce</title>
<link rel="stylesheet" href="https://fonts.googleapis.com/css2?family=Work+Sans:wght@400;500;600;700&family=Rubik:wght@500;700&display=swap">
<style>
:root{
  --green:#6aae2e;
  --green-dark:#5a9a22;
  --black:#000;
  --hero-bg:#f2f3f8;
  --section-bg:#f8fcf4;
  --text:#222;
  --muted:#555;
  --rule:#c9c9c9;
  --white:#fff;
}
*{box-sizing:border-box;margin:0;padding:0}
html,body{width:1200px;height:2469px;overflow:hidden}
body{font-family:"Work Sans",sans-serif;color:var(--text);position:relative;background:var(--section-bg)}
.abs{position:absolute}

.topbar{left:0;top:0;width:1200px;height:94px;background:var(--black);z-index:1}
.brand{left:0;top:14px;width:1200px;text-align:center;color:var(--green);font-size:36px;font-weight:600;letter-spacing:1px;z-index:3}
.mainnav{left:45px;top:70px;width:1110px;height:60px;background:var(--green);color:var(--white);font-weight:600;font-size:17px;letter-spacing:.3px;z-index:3}
.nav-item{position:absolute;display:flex;flex-direction:column;align-items:center;line-height:20px}
.nav-item svg{margin-bottom:2px}

.hero{left:0;top:94px;width:1200px;height:451px;background:var(--hero-bg)}
.hero-art{left:660px;top:130px}
.eyebrow{left:145px;top:233px;font-size:17px;font-weight:500}
.hero-title{left:145px;top:262px;width:540px;font-size:29px;line-height:35px;font-weight:600;color:var(--green)}
.btn-outline{left:144px;top:392px;width:123px;height:45px;border:2px solid #999;color:var(--green);font-size:17px;display:flex;align-items:center;justify-content:center;background:var(--white)}
.btn-solid{left:296px;top:392px;width:279px;height:45px;background:var(--green);color:var(--white);font-size:17px;font-weight:500;display:flex;align-items:center;justify-content:center;gap:12px;box-shadow:0 3px 4px rgba(0,0,0,.2)}
.btn-solid b{font-weight:700}

.section-title{left:0;width:1200px;text-align:center;color:var(--green);font-family:"Rubik",sans-serif;font-weight:700;font-size:34px;letter-spacing:1px}
.sub-title{font-family:"Rubik",sans-serif;font-weight:700;font-size:29px;color:var(--green)}

.accordion{width:445px}
.acc-head{display:flex;align-items:center;height:52px;border-bottom:1px solid var(--rule);color:var(--green);font-size:24px;font-weight:500}
.acc-head .tick{margin-right:14px}
.acc-head .chev{margin-left:auto;margin-right:162px}
.acc-open .acc-head{border-bottom:none;height:48px}
.acc-body{font-size:14px;line-height:22px;color:var(--muted);text-align:justify;letter-spacing:.3px;padding-bottom:6px;border-bottom:1px solid var(--rule)}

.pill{height:45px;border-radius:23px;background:var(--green);color:var(--white);font-weight:600;font-size:17px;display:flex;align-items:center;justify-content:center;box-shadow:0 3px 4px rgba(0,0,0,.2)}

.card{top:1950px;width:210px;text-align:center}
.card-img{width:210px;height:205px}
.card h3{font-size:22px;font-weight:500;margin-top:14px}
.card p{font-size:14px;line-height:22px;color:var(--muted);text-align:justify;margin-top:4px;letter-spacing:.3px}
.card .detail{width:102px;height:25px;margin:16px auto 0;border-radius:13px;background:var(--green);color:var(--white);font-size:14px;font-weight:600;display:flex;align-items:center;justify-content:center;box-shadow:0 2px 3px rgba(0,0,0,.2)}
.arrow{top:2030px}

.footer{left:0;top:2398px;width:1200px;height:71px;background:var(--green);color:var(--white);font-size:17px;font-weight:500;display:flex;align-items:center;justify-content:center}
</style>
</head>
<body>

<section class="abs hero"></section>
<svg class="abs hero-art" width="500" height="390" role="img" aria-label="Paper bag spilling fresh fruit, vegetables and nuts">
  <defs><radialGradient id="hg" cx="50%" cy="45%" r="55%"><stop offset="0" stop-color="#e98a3a"/><stop offset=".5" stop-color="#b5a05a"/><stop offset="1" stop-color="#f2f3f8"/></radialGradient></defs>
  <ellipse cx="260" cy="180" rx="240" ry="200" fill="url(#hg)"/>
</svg>

<header>
  <div class="abs topbar"></div>
  <div class="abs brand">BRIGHTACRE</div>
  <nav class="abs mainnav">
    <div class="nav-item" style="left:100px;top:8px">
      <svg width="26" height="22" viewBox="0 0 26 22"><path d="M13 1 1 12h4v9h6v-6h4v6h6v-9h4z" fill="#fff"/></svg>HOME</div>
    <div class="nav-item" style="left:317px;top:20px">CURRENT OFFER</div>
    <div class="nav-item" style="left:506px;top:20px">FARM DIRECTORY</div>
    <div class="nav-item" style="left:703px;top:20px">SETTINGS</div>
    <div class="nav-item" style="left:955px;top:6px">
      <svg width="22" height="24" viewBox="0 0 22 26"><circle cx="11" cy="7" r="6" fill="#fff"/><path d="M1 25c0-7 4-11 10-11s10 4 10 11z" fill="#fff"/></svg>LOGIN</div>
  </nav>
</header>

<p class="abs eyebrow">About Brightacre</p>
<h1 class="abs hero-title">Founded in 2020, Brightacre.com empowering farmers by providing market access and financial access</h1>
<a class="abs btn-outline">Read More</a>
<a class="abs btn-solid"><span>Browse <b>Fresh Products</b></span>
  <svg width="30" height="26" viewBox="0 0 30 26"><path d="M1 2h5l4 15h15l3-11H8" fill="none" stroke="#fff" stroke-width="3"/><circle cx="12" cy="22" r="2.5" fill="#fff"/><circle cx="23" cy="22" r="2.5" fill="#fff"/></svg></a>

<h2 class="abs section-title" style="top:592px">WHY BRIGHTACRE ?</h2>

<svg class="abs" style="left:140px;top:738px" width="410" height="340" role="img" aria-label="Smiling shopper handing a red pepper at a vegetable market stall">
  <defs><linearGradient id="g1" x1="0" y1="0" x2="0" y2="1"><stop offset="0" stop-color="#b89a8a"/><stop offset=".6" stop-color="#7f8a5a"/><stop offset="1" stop-color="#3b3f2a"/></linearGradient></defs>
  <path d="M120 20C200-10 320 20 360 80c40 60 50 120 40 170-20 80-120 70-220 80S20 340 6 280C-8 210 60 160 70 110 80 60 90 30 120 20z" fill="var(--green)" transform="translate(3,6)"/>
  <path d="M120 20C200-10 320 20 360 80c40 60 50 120 40 170-20 80-120 70-220 80S20 340 6 280C-8 210 60 160 70 110 80 60 90 30 120 20z" fill="url(#g1)"/>
</svg>

<h3 class="abs sub-title" style="left:616px;top:688px">Benefit for Customer</h3>
<div class="abs accordion" style="left:616px;top:745px">
  <div class="acc-open">
    <div class="acc-head"><svg class="tick" width="16" height="16" viewBox="0 0 16 16"><circle cx="8" cy="8" r="8" fill="var(--green)"/><path d="M4 8l3 3 5-6" fill="none" stroke="#fff" stroke-width="2"/></svg>Fresh Products<svg class="chev" width="18" height="12" viewBox="0 0 18 12"><path d="M2 10 9 3l7 7" fill="none" stroke="var(--green)" stroke-width="3"/></svg></div>
    <p class="acc-body">Lorem ipsum dolor sit amet, consectetur adipiscing elit. Aliquam dignissim mollis justo id ornare. Sed vitae dui vel urna convallis facilisis. Fusce quis dignissim magna, in malesuada leo. Donec condimentum in risus non cursus. Mauris commodo, felis non placerat aliquam.</p>
  </div>
  <div class="acc-head"><svg class="tick" width="16" height="16" viewBox="0 0 16 16"><circle cx="8" cy="8" r="8" fill="var(--green)"/><path d="M4 8l3 3 5-6" fill="none" stroke="#fff" stroke-width="2"/></svg>Best Prices<svg class="chev" width="18" height="12" viewBox="0 0 18 12"><path d="M2 2l7 7 7-7" fill="none" stroke="var(--green)" stroke-width="3"/></svg></div>
  <div class="acc-head"><svg class="tick" width="16" height="16" viewBox="0 0 16 16"><circle cx="8" cy="8" r="8" fill="var(--green)"/><path d="M4 8l3 3 5-6" fill="none" stroke="#fff" stroke-width="2"/></svg>Fresh Products<svg class="chev" width="18" height="12" viewBox="0 0 18 12"><path d="M2 2l7 7 7-7" fill="none" stroke="var(--green)" stroke-width="3"/></svg></div>
  <div class="acc-head"><svg class="tick" width="16" height="16" viewBox="0 0 16 16"><circle cx="8" cy="8" r="8" fill="var(--green)"/><path d="M4 8l3 3 5-6" fill="none" stroke="#fff" stroke-width="2"/></svg>Best Prices<svg class="chev" width="18" height="12" viewBox="0 0 18 12"><path d="M2 2l7 7 7-7" fill="none" stroke="var(--green)" stroke-width="3"/></svg></div>
  <div class="acc-head"><svg class="tick" width="16" height="16" viewBox="0 0 16 16"><circle cx="8" cy="8" r="8" fill="var(--green)"/><path d="M4 8l3 3 5-6" fill="none" stroke="#fff" stroke-width="2"/></svg>Fresh Products<svg class="chev" width="18" height="12" viewBox="0 0 18 12"><path d="M2 2l7 7 7-7" fill="none" stroke="var(--green)" stroke-width="3"/></svg></div>
</div>
<a class="abs pill" style="left:718px;top:1151px;width:267px">Browse Fresh Products</a>

<h3 class="abs sub-title" style="left:145px;top:1262px">Benefit for Farmer</h3>
<div class="abs accordion" style="left:145px;top:1319px">
  <div class="acc-open">
    <div class="acc-head"><svg class="tick" width="16" height="16" viewBox="0 0 16 16"><circle cx="8" cy="8" r="8" fill="var(--green)"/><path d="M4 8l3 3 5-6" fill="none" stroke="#fff" stroke-width="2"/></svg>Market Access<svg class="chev" width="18" height="12" viewBox="0 0 18 12"><path d="M2 10 9 3l7 7" fill="none" stroke="var(--green)" stroke-width="3"/></svg></div>
    <p class="acc-body">Lorem ipsum dolor sit amet, consectetur adipiscing elit. Aliquam dignissim mollis justo id ornare. Sed vitae dui vel urna convallis facilisis. Fusce quis dignissim magna, in malesuada leo. Donec condimentum in risus non cursus. Mauris commodo, felis non placerat aliquam.</p>
  </div>
  <div class="acc-head"><svg class="tick" width="16" height="16" viewBox="0 0 16 16"><circle cx="8" cy="8" r="8" fill="var(--green)"/><path d="M4 8l3 3 5-6" fill="none" stroke="#fff" stroke-width="2"/></svg>Financial Access<svg class="chev" width="18" height="12" viewBox="0 0 18 12"><path d="M2 2l7 7 7-7" fill="none" stroke="var(--green)" stroke-width="3"/></svg></div>
  <div class="acc-head"><svg class="tick" width="16" height="16" viewBox="0 0 16 16"><circle cx="8" cy="8" r="8" fill="var(--green)"/><path d="M4 8l3 3 5-6" fill="none" stroke="#fff" stroke-width="2"/></svg>Market Access<svg class="chev" width="18" height="12" viewBox="0 0 18 12"><path d="M2 2l7 7 7-7" fill="none" stroke="var(--green)" stroke-width="3"/></svg></div>
  <div class="acc-head"><svg class="tick" width="16" height="16" viewBox="0 0 16 16"><circle cx="8" cy="8" r="8" fill="var(--green)"/><path d="M4 8l3 3 5-6" fill="none" stroke="#fff" stroke-width="2"/></svg>Financial Access<svg class="chev" width="18" height="12" viewBox="0 0 18 12"><path d="M2 2l7 7 7-7" fill="none" stroke="var(--green)" stroke-width="3"/></svg></div>
  <div class="acc-head"><svg class="tick" width="16" height="16" viewBox="0 0 16 16"><circle cx="8" cy="8" r="8" fill="var(--green)"/><path d="M4 8l3 3 5-6" fill="none" stroke="#fff" stroke-width="2"/></svg>Market Access<svg class="chev" width="18" height="12" viewBox="0 0 18 12"><path d="M2 2l7 7 7-7" fill="none" stroke="var(--green)" stroke-width="3"/></svg></div>
</div>
<a class="abs pill" style="left:247px;top:1725px;width:267px">Tell Me More</a>

<svg class="abs" style="left:650px;top:1372px" width="415" height="265" role="img" aria-label="Silhouettes of two farmers shaking hands in a field at sunset">
  <defs><linearGradient id="g2" x1="0" y1="0" x2="0" y2="1"><stop offset="0" stop-color="#d9a77a"/><stop offset=".55" stop-color="#8a5a36"/><stop offset="1" stop-color="#2b1a10"/></linearGradient></defs>
  <path d="M180 5c90-10 170 30 200 70 40 50 40 120 0 160-40 40-110 10-170-20-60-30-120 30-170 20C0 225 0 170 20 130 50 70 100 15 180 5z" fill="var(--green)" transform="translate(2,6)"/>
  <path d="M180 5c90-10 170 30 200 70 40 50 40 120 0 160-40 40-110 10-170-20-60-30-120 30-170 20C0 225 0 170 20 130 50 70 100 15 180 5z" fill="url(#g2)"/>
</svg>

<h2 class="abs section-title" style="top:1872px">FEATURED FARM AND PRODUCTS</h2>

<svg class="abs arrow" style="left:64px" width="50" height="50" viewBox="0 0 50 50"><circle cx="25" cy="25" r="23" fill="none" stroke="var(--green)" stroke-width="3"/><path d="M29 14 18 25l11 11" fill="none" stroke="var(--green)" stroke-width="3"/></svg>
<svg class="abs arrow" style="left:1085px" width="50" height="50" viewBox="0 0 50 50"><circle cx="25" cy="25" r="23" fill="none" stroke="var(--green)" stroke-width="3"/><path d="M21 14l11 11-11 11" fill="none" stroke="var(--green)" stroke-width="3"/></svg>

<article class="abs card" style="left:143px">
  <div class="card-img" role="img" aria-label="Bunch of ripe tomatoes on the vine" style="background:radial-gradient(circle,#d6261c 0%,#e84a3a 55%,#fff 75%)"></div>
  <h3>Tomato</h3>
  <p>Lorem ipsum dolor sit amet, consectetur adipiscing elit. Aliquam...</p>
  <a class="detail">Detail</a>
</article>
<article class="abs card" style="left:378px">
  <div class="card-img" role="img" aria-label="Pile of organic potatoes with slices" style="background:radial-gradient(circle,#d8b864 0%,#e6cf8c 55%,#fff 78%)"></div>
  <h3>Organic Potato</h3>
  <p>Lorem ipsum dolor sit amet, consectetur adipiscing elit. Aliquam...</p>
  <a class="detail">Detail</a>
</article>
<article class="abs card" style="left:611px">
  <div class="card-img" role="img" aria-label="Two fresh strawberries" style="background:radial-gradient(circle,#d8141e 0%,#e63a3a 50%,#fff 72%)"></div>
  <h3>Strawberry</h3>
  <p>Lorem ipsum dolor sit amet, consectetur adipiscing elit. Aliquam...</p>
  <a class="detail">Detail</a>
</article>
<article class="abs card" style="left:846px">
  <div class="card-img" role="img" aria-label="Corn cobs with green husks" style="background:linear-gradient(160deg,#f5c400 0%,#f2d43a 55%,#6bb33a 85%,#fff 100%)"></div>
  <h3>Corn</h3>
  <p>Lorem ipsum dolor sit amet, consectetur adipiscing elit. Aliquam...</p>
  <a class="detail">Detail</a>
</article>

<footer class="abs footer">Brightacre. All right reserved.</footer>

</body>
</html>
```